Mental Health care Company in Washington DC

We are a new mental health care services provider in Washington DC. Please look at these sites.
https://marlowbrookpartners.com
https://www.quillstoneinc.com
https://velmarsh-kt.org/
https://www.trivanqx.com
https://www.thelanternofqz.com

```html
<!DOCTYPE html>
<html lang="en">
<head>
<meta charset="utf-8">
<title>Orla Health Services</title>
<link href="https://fonts.googleapis.com/css2?family=Outfit:wght@400;500;600;700&family=Questrial&display=swap" rel="stylesheet">
<style>
:root{
  --navy:#0f1e45;
  --orange:#f5a462;
  --teal:#a3d9dc;
  --text:#4a4a4a;
  --white:#ffffff;
  --head:'Outfit',sans-serif;
  --body:'Questrial',sans-serif;
}
*{margin:0;padding:0;box-sizing:border-box}
html,body{width:1200px;height:4389px;overflow:hidden;background:var(--white)}
.page{position:relative;width:1200px;height:4389px;font-family:var(--body);color:var(--text)}
.btn{position:absolute;display:flex;align-items:center;justify-content:center;border-radius:10px;font-family:var(--head);font-weight:500;color:var(--white);background:var(--orange);font-size:16px;text-decoration:none}
.btn.teal{background:var(--teal)}
.ph{position:absolute}

/* header */
.site-header{position:absolute;top:0;left:0;width:1200px;height:102px;border-top:5px solid var(--orange);background:var(--white)}
.brand{position:absolute;left:85px;top:38px;display:flex;align-items:center;gap:10px;font-family:var(--head);color:var(--navy);font-weight:600;font-size:23px;line-height:1;white-space:nowrap}
.brand-dot{width:12px;height:12px;border-radius:50%;background:var(--orange);flex:none}
.nav a{position:absolute;top:46px;font-family:var(--head);font-size:16px;font-weight:500;color:var(--navy);text-decoration:none}
.nav a.active{color:var(--orange)}

/* hero */
.hero{position:absolute;top:102px;left:0;width:1200px;height:541px;background:linear-gradient(100deg,#5d4a3e 0%,#8c7160 35%,#a68b78 60%,#d4c3b4 100%)}
.hero::after{content:"";position:absolute;inset:0;background:rgba(40,30,25,.35)}
.hero-sub{position:absolute;top:160px;width:100%;text-align:center;color:var(--white);font-family:var(--head);font-weight:400;font-size:38px;z-index:1}
.hero-title{position:absolute;top:212px;width:100%;text-align:center;color:var(--white);font-family:var(--head);font-weight:700;font-size:62px;z-index:1}
.hero .btn{z-index:1;left:494px;top:305px;width:210px;height:48px;font-size:17px;border-radius:14px}

/* services */
.eyebrow{position:absolute;top:745px;width:100%;text-align:center;color:var(--teal);font-family:var(--head);letter-spacing:3px;font-size:17px;font-weight:500}
.section-title{position:absolute;width:100%;text-align:center;font-family:var(--head);font-weight:600;color:var(--navy);font-size:46px}
.card{position:absolute;top:868px;width:319px;height:443px;background:var(--white);border-radius:34px 34px 0 34px;box-shadow:0 6px 18px rgba(0,0,0,.12);overflow:hidden}
.card .ph{left:0;top:0;width:319px;height:216px}
.card h3{position:absolute;left:22px;top:234px;font-family:var(--head);font-weight:600;font-size:25px;line-height:29px;color:var(--navy)}
.card p{position:absolute;left:22px;top:306px;width:250px;font-size:15px;line-height:20px;color:var(--text)}
.card .btn{left:22px;top:382px;width:104px;height:34px;font-size:14px;border-radius:10px}

/* welcome */
.welcome{position:absolute;top:1491px;left:0;width:1200px;height:565px;background:var(--teal)}
.band-title{position:absolute;font-family:var(--head);font-weight:600;font-size:38px;line-height:42px;color:var(--white)}
.band-text{position:absolute;width:350px;font-size:16px;line-height:25px;color:var(--white)}

/* care team */
.care-title{position:absolute;left:707px;top:2227px;font-family:var(--head);font-weight:600;font-size:38px;color:var(--navy)}
.care-text{position:absolute;left:716px;top:2294px;width:360px;font-size:16px;line-height:25px;color:var(--text)}

/* insurance */
.insurance{position:absolute;top:2691px;left:0;width:1200px;height:536px;background:var(--orange)}

/* why */
.why h4{position:absolute;font-family:var(--head);font-weight:500;font-size:21px;color:var(--orange)}
.why p{position:absolute;width:270px;font-size:15px;line-height:21px;color:var(--text)}
.why .right-align{text-align:right}

/* footer */
.site-footer{position:absolute;top:3984px;left:0;width:1200px;height:405px;background:var(--navy);color:var(--white)}
.foot-brand{position:absolute;left:130px;top:112px;display:flex;align-items:center;gap:10px;font-family:var(--head);font-weight:600;font-size:24px;line-height:1;color:var(--white);white-space:nowrap}
.social{position:absolute;top:185px;width:33px;height:33px;background:var(--teal)}
.foot-col h5{position:absolute;top:72px;font-family:var(--head);font-weight:600;font-size:21px}
.foot-col ul{position:absolute;top:120px;list-style:none;font-size:15px;line-height:31px}
.contact-row{position:absolute;left:823px;display:flex;gap:14px;font-size:15px;line-height:18px}
.contact-row svg{flex:none}
.copyright{position:absolute;top:345px;width:100%;text-align:center;font-size:15px}
</style>
</head>
<body>
<div class="page">

<header class="site-header">
  <div class="brand"><span class="brand-dot"></span>Orla Health Services</div>
  <nav class="nav">
    <a class="active" style="left:375px" href="#">Home</a>
    <a style="left:462px" href="#">About Us</a>
    <a style="left:574px" href="#">Therapies &amp; Treatment</a>
    <a style="left:786px" href="#">Our Services</a>
    <a style="left:924px" href="#">Gallery</a>
    <a style="left:1019px" href="#">Contact Us</a>
  </nav>
</header>

<section class="hero" role="img" aria-label="Family meeting with a therapist in a warm counselling room">
  <div class="hero-sub">Orla Health Services</div>
  <div class="hero-title">We Care. For You.</div>
  <a class="btn">Make an Appointment</a>
</section>

<div class="eyebrow">OUR SERVICES</div>
<h2 class="section-title" style="top:772px">Services We Offer</h2>

<article class="card" style="left:92px">
  <div class="ph" role="img" aria-label="Person clasping hands during a consultation" style="background:linear-gradient(135deg,#8b8a6e,#c9b9a3)"></div>
  <h3>Psychiatric<br>Consultations</h3>
  <p>Lorem ipsum dolor lessit amet lorconse ctetlorur adipiscing elit cumsan lacus vel facilisis.</p>
  <a class="btn">Read More</a>
</article>
<article class="card" style="left:441px">
  <div class="ph" role="img" aria-label="Counsellor talking with a child and parent" style="background:linear-gradient(135deg,#7c8fa6,#c9a98a)"></div>
  <h3>Children and<br>Adolescent Services</h3>
  <p>Lorem ipsum dolor lessit amet lorconse ctetlorur adipiscing elit cumsan lacus vel facilisis.</p>
  <a class="btn">Read More</a>
</article>
<article class="card" style="left:789px">
  <div class="ph" role="img" aria-label="Family session with a therapist in a bright room" style="background:linear-gradient(135deg,#9aa3a8,#b8876a)"></div>
  <h3>Adult and Senior<br>Services</h3>
  <p>Lorem ipsum dolor lessit amet lorconse ctetlorur adipiscing elit cumsan lacus vel facilisis.</p>
  <a class="btn">Read More</a>
</article>

<section class="welcome">
  <h2 class="band-title" style="left:131px;top:130px">Welcome to<br>Orla Health Services</h2>
  <p class="band-text" style="left:131px;top:233px">Lorem ipsum dolor sit amet, consectetur adipiscing elit, sed do eiusmod tempor incididunt ut labore et dolore magna aliqua. Quis ipsum suspendisse ultrices gravida. Risus commodo viverra maecenas accumsan lacus vel facilisis.</p>
  <a class="btn" style="left:131px;top:406px;width:145px;height:48px;border-radius:14px">Read More</a>
  <div class="ph" role="img" aria-label="Therapist listening to a client" style="left:559px;top:0;width:402px;height:420px;border-radius:0 0 201px 201px;background:linear-gradient(160deg,#7d8a6a,#c99a4a)"></div>
  <div class="ph" role="img" aria-label="Smiling woman talking in a counselling session" style="left:920px;top:270px;width:280px;height:295px;border-radius:140px 0 0 0;background:linear-gradient(160deg,#b7b3ad,#7a8aa8)"></div>
</section>

<div class="ph" role="img" aria-label="Hands held in support" style="left:112px;top:2192px;width:214px;height:251px;border-radius:0 0 0 107px;background:linear-gradient(135deg,#e9ddd6,#c7967f)"></div>
<div class="ph" style="left:128px;top:2463px;width:181px;height:102px;border-radius:90px 90px 0 0;background:var(--teal)"></div>
<div class="ph" role="img" aria-label="Young woman speaking with a counsellor holding a tablet" style="left:338px;top:2189px;width:308px;height:363px;border-radius:154px 154px 0 0;background:linear-gradient(160deg,#7e9b6b,#d9d2cc)"></div>
<h2 class="care-title">Your Care Team</h2>
<p class="care-text">Lorem ipsum dolor sit amet, consectetur adipiscing elit, sed do eiusmod tempor incididunt ut labore et dolore magna aliqua. Quis ipsum suspendisse ultrices gravida. Risus commodo viverra maecenas accumsan lacus vel facilisis.</p>
<a class="btn" style="left:716px;top:2460px;width:210px;height:46px;border-radius:14px">Make an Appointment</a>

<section class="insurance">
  <h2 class="band-title" style="left:128px;top:120px">Works with<br>Your insurance</h2>
  <p class="band-text" style="left:128px;top:212px">Lorem ipsum dolor sit amet, consectetur adipiscing elit, sed do eiusmod tempor incididunt ut labore et dolore magna aliqua. Quis ipsum suspendisse ultrices gravida. Risus commodo viverra maecenas accumsan lacus vel facilisis.</p>
  <a class="btn teal" style="left:128px;top:386px;width:129px;height:46px;border-radius:14px">Read More</a>
  <div class="ph" role="img" aria-label="Mother and daughter embracing" style="left:559px;top:0;width:641px;height:536px;border-radius:260px 0 0 260px;background:linear-gradient(120deg,#5d7a5a,#c39a5c 60%,#e0d5c8)"></div>
</section>

<section class="why">
  <h2 class="section-title" style="top:3326px">Why Choose Us?</h2>
  <div class="ph" role="img" aria-label="Counsellor holding a notebook" style="left:542px;top:3414px;width:104px;height:183px;border-radius:52px 52px 0 0;background:linear-gradient(#b9c6d6,#7f91ad)"></div>
  <div class="ph" role="img" aria-label="Child resting" style="left:360px;top:3597px;width:182px;height:104px;border-radius:52px 0 0 52px;background:linear-gradient(90deg,#d9d3cc,#7a5a48)"></div>
  <div class="ph" role="img" aria-label="Hands held together" style="left:646px;top:3597px;width:181px;height:104px;border-radius:0 52px 52px 0;background:linear-gradient(90deg,#a88a76,#d9c3b5)"></div>
  <div class="ph" role="img" aria-label="Thoughtful young woman" style="left:542px;top:3701px;width:104px;height:182px;border-radius:0 0 52px 52px;background:linear-gradient(#a9a39c,#6f7d8a)"></div>

  <h4 style="left:221px;top:3447px;width:270px;text-align:right">Adipiscing elit losed do</h4>
  <p class="right-align" style="left:221px;top:3480px">Lorem ipsum dolor sit amet, consectetur adipiscing elit, sed do eiusmod tempor incididunt ut labore et.</p>
  <h4 style="left:697px;top:3447px">Adipiscing elit losed do</h4>
  <p style="left:697px;top:3480px">Lorem ipsum dolor sit amet, consectetur adipiscing elit, sed do eiusmod tempor incididunt ut labore et.</p>
  <h4 style="left:221px;top:3750px;width:270px;text-align:right">Adipiscing elit losed do</h4>
  <p class="right-align" style="left:221px;top:3783px">Lorem ipsum dolor sit amet, consectetur adipiscing elit, sed do eiusmod tempor incididunt ut labore et.</p>
  <h4 style="left:697px;top:3750px">Adipiscing elit losed do</h4>
  <p style="left:697px;top:3783px">Lorem ipsum dolor sit amet, consectetur adipiscing elit, sed do eiusmod tempor incididunt ut labore et.</p>
</section>

<footer class="site-footer">
  <div class="foot-brand"><span class="brand-dot"></span>Orla Health Services</div>
  <span class="social" style="left:205px" aria-label="Social profile"></span>
  <span class="social" style="left:247px" aria-label="Social profile"></span>

  <div class="foot-col">
    <h5 style="left:430px">Menu</h5>
    <ul style="left:430px"><li>Home</li><li>Our Services</li><li>Insurance</li><li>Testimonials</li><li>About</li><li>Contact</li></ul>
    <h5 style="left:600px">Services</h5>
    <ul style="left:600px"><li>Medical Services</li><li>Behavioral Health</li><li>Human Services</li><li>Spiritual Needs</li><li>Other Services</li></ul>
    <h5 style="left:823px">Contact</h5>
  </div>

  <div class="contact-row" style="top:120px">
    <svg width="36" height="36" viewBox="0 0 36 36"><rect width="36" height="36" rx="8" fill="#f5a462"/><path d="M18 8a7 7 0 0 0-7 7c0 5 7 12 7 12s7-7 7-12a7 7 0 0 0-7-7z" fill="none" stroke="#fff" stroke-width="2"/><circle cx="18" cy="15" r="2.5" fill="none" stroke="#fff" stroke-width="2"/></svg>
    <div>Orla Health Services<br>Harbor Lane 14, Suite 2B</div>
  </div>
  <div class="contact-row" style="top:173px">
    <svg width="36" height="36" viewBox="0 0 36 36"><rect width="36" height="36" rx="8" fill="#f5a462"/><path d="M12 9l4 1 1 5-2 2a11 11 0 0 0 4 4l2-2 5 1 1 4-2 2c-8 0-15-7-15-15z" fill="none" stroke="#fff" stroke-width="2" stroke-linejoin="round"/></svg>
    <div>Phone:<br>555 0142 318</div>
  </div>
  <div class="contact-row" style="top:228px">
    <svg width="36" height="36" viewBox="0 0 36 36"><rect width="36" height="36" rx="8" fill="#f5a462"/><rect x="9" y="11" width="18" height="14" rx="2" fill="none" stroke="#fff" stroke-width="2"/><path d="M9 12l9 7 9-7" fill="none" stroke="#fff" stroke-width="2"/></svg>
    <div>Email:<br>hello@orlahealth.example</div>
  </div>

  <div class="copyright">© 2025 Copyright - Orla Health Services. All Rights are Reserved.</div>
</footer>

</div>
</body>
</html>
```